We need a business card for our gym. We are a LiftCore affiliate in Halvern Georgie established 2008. Our company name is Tarn Functional Fitness. LiftCore Shaping Peak Fitness. Instagram and website is @tarnhall. Hashtags we use #lifewithgrit #madetolift We want something similar to the the black and neon green design attached but a different color scheme. No neon colors. Are company colors are the same as the blue and white card attached. We are open to ideas as far as colors however - just no neon.

Contact Information for Business Card

Tarn Functional Fitness
427 Pellow Drive
Halvern WM 30817
Phone 404.555.0186 Website www.tarnhall.example

Font styles to use
Other font styles liked:
• Futura Extra Bold Condensed

Colors

Designer to choose colors to be used in the design.

Requirements
Must have
• Our primary font we typically use for our name is Futura Extra Bold Condensed
Nice to have
• I attached a card from that is black and neon green from Vexa that we would like something similar. The blue and white is more similar to our colors. We also use have used black and white in the past. We use the chevrons as out logo. We are a LiftCore affiliate so I included a logo from them as well that may or may not be used on the card. Our instagram is @tarnhall hashtags #madetolift #lifewithgrit
Should not have
• No neon colors

```html
<!DOCTYPE html>
<html lang="en">
<head>
<meta charset="utf-8">
<title>Tarn Functional Fitness – Business Card</title>
<link href="https://fonts.googleapis.com/css2?family=Jost:wght@400;500;600;800&display=swap" rel="stylesheet">
<style>
  :root {
    --bg: #d4d5d7;
    --card-black: #0a0b0d;
    --brand-blue: #4a7fb0;
    --white: #f4f5f6;
    --shadow: rgba(0,0,0,0.28);
  }
  * { box-sizing: border-box; margin: 0; padding: 0; }
  html, body { width: 1200px; height: 1021px; overflow: hidden; }
  body {
    background: var(--bg);
    font-family: "Jost", sans-serif;
    color: var(--white);
    display: flex;
    flex-direction: column;
    align-items: center;
    justify-content: center;
    gap: 48px;
  }
  .card {
    width: 760px;
    height: 434px;
    position: relative;
    box-shadow: 0 10px 26px var(--shadow);
  }
  /* Front */
  .card-front {
    background: var(--card-black);
    border-bottom: 5px solid var(--brand-blue);
    display: flex;
    flex-direction: column;
    align-items: center;
    justify-content: center;
  }
  .brand-name {
    font-weight: 800;
    color: var(--white);
    text-transform: uppercase;
    line-height: 0.95;
    text-align: center;
  }
  .brand-name .big { display: block; font-size: 112px; letter-spacing: 2px; }
  .brand-name .small { display: block; font-size: 38px; letter-spacing: 1px; }
  .location {
    margin-top: 14px;
    color: var(--brand-blue);
    font-weight: 500;
    letter-spacing: 12px;
    font-size: 24px;
    text-transform: uppercase;
  }
  /* Back */
  .card-back {
    background: var(--brand-blue);
    padding: 24px;
  }
  .back-inner {
    background: var(--card-black);
    width: 100%;
    height: 100%;
    position: relative;
  }
  .back-brand {
    position: absolute;
    left: 70px;
    top: 52px;
    text-align: left;
  }
  .back-brand .brand-name { text-align: left; }
  .back-brand .brand-name .big { font-size: 72px; }
  .back-brand .brand-name .small { font-size: 24px; }
  .back-brand .location { font-size: 15px; letter-spacing: 8px; margin-top: 8px; }
  .affiliate {
    position: absolute;
    left: 70px;
    top: 230px;
    font-weight: 800;
    color: var(--white);
    line-height: 1;
  }
  .affiliate .name { display: block; font-size: 34px; }
  .affiliate .tag { display: block; font-size: 11px; text-transform: uppercase; letter-spacing: 0.5px; }
  .hashtags {
    position: absolute;
    left: 0; right: 0;
    bottom: 26px;
    text-align: center;
    font-size: 20px;
    font-weight: 500;
    letter-spacing: 3px;
  }
  .contact {
    position: absolute;
    left: 450px;
    top: 118px;
    font-size: 18px;
    font-weight: 500;
    line-height: 1.35;
  }
  .contact .person { color: var(--brand-blue); font-size: 26px; font-weight: 600; line-height: 1.1; }
  .contact .role { font-size: 17px; margin-bottom: 22px; }
  .contact .row { display: flex; align-items: center; gap: 8px; margin-left: -24px; }
  .contact .row svg { width: 16px; height: 16px; flex: none; }
</style>
</head>
<body>
  <section class="card card-front">
    <div class="brand-name"><span class="big">Tarn</span><span class="small">Functional Fitness</span></div>
    <div class="location">Halvern • Westmark</div>
  </section>

  <section class="card card-back">
    <div class="back-inner">
      <div class="back-brand">
        <div class="brand-name"><span class="big">Tarn</span><span class="small">Functional Fitness</span></div>
        <div class="location">Halvern • Westmark</div>
      </div>
      <div class="affiliate"><span class="name">LiftCore</span><span class="tag">Shaping Peak Fitness</span></div>

      <div class="contact">
        <div class="person">Dorian Hale</div>
        <div class="role">Founder</div>
        <div>427 Pellow Drive</div>
        <div>Halvern WM 30817</div>
        <div class="row">
          <svg viewBox="0 0 16 16" aria-hidden="true"><path d="M3 1.5l3 .5 1 3.5-2 1.2c.8 1.8 2 3 3.8 3.8L10 8.5l3.5 1 .5 3-1.5 2C7 14.5 1.5 9 1.5 3z" fill="var(--brand-blue)"/></svg>
          <span>404.555.0186</span>
        </div>
        <div class="row">
          <svg viewBox="0 0 16 16" aria-hidden="true" fill="none" stroke="var(--brand-blue)" stroke-width="1.3"><circle cx="8" cy="8" r="6.5"/><ellipse cx="8" cy="8" rx="3" ry="6.5"/><line x1="1.5" y1="8" x2="14.5" y2="8"/></svg>
          <span>www.tarnhall.example</span>
        </div>
        <div class="row">
          <svg viewBox="0 0 16 16" aria-hidden="true"><rect x="2" y="2" width="12" height="12" fill="none" stroke="var(--brand-blue)" stroke-width="1.4"/></svg>
          <span>@tarnhall</span>
        </div>
      </div>

      <div class="hashtags">#lifewithgrit&nbsp;&nbsp;•&nbsp;&nbsp;#madetolift</div>
    </div>
  </section>
</body>
</html>
```